"ZENTRAL BEAT" - German Rap Concert

Hello,

I need a Flyer for a concert in Reutlingen, Germany.
The following Information should be included in the Flyer:

"ZENTRAL BEAT

09.01.2015
Beginn: 17:00 Uhr
Einlass: 15:30 Uhr

Acts:
OLU BRANDT
Mira Quell
Rotfeld & SolarBoy
RUV
Salihu. PNW & Luppo
TwoStep

VVK: 26€

Klangwerk, Lindenweg 14, 72760 Reutlingen"

The Logo of the Location should also be in the Flyer.
Main Act is Olu Brandt. you can find a Picture of him attached.
We also need space for Sponsoring-logos (4) at the bottom of the Flyer.
The Logos of the Sponsors will come later.

I hope you can understand my english ;)
If you have any questions, just write me an email.

Thanks in advance!

Tobias

Edit: The size of the Flyer should be DinA6.
I have also uploaded a better Version of the Klangwerk Logo!
Updates

Dear Designers, I have uploaded 3 of the 4 Sponsoring-Logos. Please insert them into the Flyer! Sponsors: LDR-S (please write under the logo "Sport- & Eventmanagement") Moos Brauerei Wendlinger Thanks!

```html
<!DOCTYPE html>
<html lang="de">
<head>
<meta charset="utf-8">
<title>Zentral Beat – Flyer</title>
<link rel="stylesheet" href="https://fonts.googleapis.com/css2?family=Open+Sans:wght@400;600;700;800&display=swap">
<style>
  :root {
    --page-bg: #d6d6d6;
    --flyer-bg: #05050b;
    --teal: #6cc4bb;
    --white: #ffffff;
    --muted: #6f6f72;
    --logo-ink: #2a2e33;
    --photo-dark: #0c0c12;
    --photo-mid: #3a2f2c;
    --photo-light: #7a6558;
  }
  * { margin: 0; padding: 0; box-sizing: border-box; }
  html, body {
    width: 1200px; height: 900px; overflow: hidden;
    background: var(--page-bg);
    font-family: "Open Sans", Arial, sans-serif;
  }
  .flyer {
    position: absolute; left: 120px; top: 107px;
    width: 960px; height: 683px;
    background: var(--flyer-bg);
    overflow: hidden;
    box-shadow: 0 6px 24px rgba(0,0,0,0.35);
  }
  .artist-photo {
    position: absolute; left: 0; top: 0;
    width: 392px; height: 683px;
    background: radial-gradient(ellipse at 45% 35%, var(--photo-light) 0%, var(--photo-mid) 35%, var(--photo-dark) 75%);
  }
  .venue-logo {
    position: absolute; left: 692px; top: -132px;
    width: 270px; height: 270px; border-radius: 50%;
    background: var(--white);
  }
  .venue-logo span {
    position: absolute; left: 0; right: 0; top: 168px;
    text-align: center;
    font-weight: 800; font-size: 33px; letter-spacing: 0.5px;
    color: var(--logo-ink);
  }
  .event-title {
    position: absolute; left: 398px; top: 60px;
    font-size: 34px; font-weight: 600; color: var(--teal);
  }
  .acts-label {
    position: absolute; left: 400px; top: 126px;
    font-size: 13px; font-weight: 700; color: var(--white);
  }
  .acts {
    position: absolute; left: 397px; top: 138px;
    list-style: none; color: var(--white); font-weight: 700;
  }
  .acts li { font-size: 33px; line-height: 43.5px; }
  .acts .headliner { font-size: 46px; line-height: 56px; letter-spacing: 0.5px; }
  .event-time {
    position: absolute; left: 709px; top: 150px;
    font-size: 16px; line-height: 21.5px; color: var(--muted);
  }
  .presale {
    position: absolute; left: 398px; top: 440px;
    font-size: 24px; font-weight: 700; color: var(--teal);
  }
  .address {
    position: absolute; left: 399px; top: 492px;
    font-size: 16px; color: var(--muted);
  }
  .sponsors {
    position: absolute; left: 398px; top: 570px;
    width: 520px; height: 95px;
  }
  .sponsor {
    position: absolute; color: var(--white);
    font-weight: 700; text-align: center;
  }
  .sponsor-ldrs { left: 0; top: 22px; width: 170px; }
  .sponsor-ldrs .name { font-size: 20px; display: block; }
  .sponsor-ldrs .note { font-size: 13px; font-weight: 400; display: block; margin-top: 2px; }
  .sponsor-moos { left: 195px; top: 34px; width: 125px; font-size: 17px; }
  .sponsor-wendlinger {
    left: 345px; top: 20px; width: 162px; height: 40px;
    display: flex; align-items: center; justify-content: center; gap: 8px;
    font-size: 19px;
  }
  .sponsor-wendlinger .mark { width: 10px; height: 10px; background: var(--white); }
</style>
</head>
<body>
  <main class="flyer">
    <div class="artist-photo" role="img" aria-label="Portrait of headliner Olu Brandt wearing sunglasses and a mesh jersey"></div>

    <div class="venue-logo"><span>KLANGWERK</span></div>

    <h1 class="event-title">ZENTRAL BEAT</h1>
    <p class="acts-label">Acts:</p>
    <ul class="acts">
      <li class="headliner">OLU BRANDT</li>
      <li>Mira Quell</li>
      <li>Rotfeld &amp; SolarBoy</li>
      <li>RUV</li>
      <li>Salihu. PNW &amp; Luppo</li>
      <li>TwoStep</li>
    </ul>

    <p class="event-time">09.01.2015<br>Beginn: 17:00 Uhr<br>Einlass: 15:30 Uhr</p>

    <p class="presale">VVK: 26€</p>
    <p class="address">Klangwerk, Lindenweg 14, 72760 Reutlingen</p>

    <footer class="sponsors">
      <div class="sponsor sponsor-ldrs">
        <span class="name">LDR-S</span>
        <span class="note">Sport- &amp; Eventmanagement</span>
      </div>
      <div class="sponsor sponsor-moos">Moos Brauerei</div>
      <div class="sponsor sponsor-wendlinger"><span class="mark"></span>Wendlinger</div>
    </footer>
  </main>
</body>
</html>
```